Design Website to Recruit next Generation of Iron Parlor's Task Force Ember

Design a cool website that provides just enough information to be intriguing to teenagers who compete in combat sports. The format is to make this an invite-only team of high-school-aged competitors in combat sports (predominately Jiu Jitsu right now). Orbit Pups can participate in similar assignments to earn consideration. We are modeled after the Task Force Ember formed in Iron Parlor and would like to keep that look and feel. The document attached "TFE - Ideas and Content for Website" shows our initial thoughts and here is more about us:

Goal - To promote the success of committed teenage Jiu Jitsu competitors who excel through focused preparation and deliberate practice.

Why - Prove the core principles of success.

How - Success is its own reward and always entails an element of the unknown/uncontrollable. We reward preparation. Setting clear goals (SMART), deliberate practice, building mental models (domain specific knowledge), restorative recovery, nutritional coaching, power of teaching others, sports science (strength & conditioning), expert guidance, personalized development plans, accountability, Quantified Self, gamification and competitive challenges. What - We will win at the highest of levels across the fight world by applying the general principles of success. These lessons will be carried with them to other areas of their lives.

Our primary goal with the website would be to share our company’s mission statement and promote the success of our sponsored athletes.

The only social media account we have currently is Instagram's @taskforceemberK7 (recently established). If you want more of an idea for what our online presence should feel like, then I would suggest watching these two scenes from Iron Parlor:

Recruiting: This scene shows the process for joining Task Force Ember: https://clipnest.tv/Qr7Lx2mPa9c

Task Force Ember Assignments: This shows how assignments are handed out for members to accomplish: https://clipnest.tv/Hw3TbN8ekVo

Task Force Ember Color Assignment: This is their first large assignment and where the green color comes from: https://clipnest.tv/Zf5uJc1RdyE

It is also worth noting that "less is more" considering the first rule is, "you do not talk about..." That should carry over to our website and social media presence. We want to share just enough to be intriguing to inquiring minds and motivational for members, but no more.

I have uploaded a bunch of content, but just wanted to give you a broader idea. Feel free to design as you see fit...
Updates

Please stay tuned for the "burning smiley face" files. I have purchased a rendering of it so we have a proprietary vector image to use on our site. There will also be files for different versions of the Task Force Ember//TFE logos for various subcategories. Here is how they are to be applied: Circled = Primary (for main/landing page), Jiu Jitsu = Pyramid, Wrestling = Traditional, Muay Thai = Rolled, and Legacy TFE = Original (coming soon).

Target Market(s)

Teenage competitors of combat sports, their parents, and sponsors of those athletes

Industry/Entity Type

Martial Arts & High School Sports

Coding

Coded - Design and coding required

Number of Pages Required

5+ page

Font styles to use
Sans Serif
Other font styles liked:
• See font in "Circled Logo"

Colors
59FF00
82FF00
B8FF75
E3FFCB
F4FFEA
EB3D1F
EC4F4E
F09395
F8D3D4
FCEDEE

Requirements
Must have
• Cool landing page with logo and brief summary of what we do. Page with 8 rules and explanation for earning an invitation. Plus, accomplishments page for memorializing the success of sponsored "Orbit Pups"
Should not have
• Individual names

```html
<!DOCTYPE html>
<html lang="en">
<head>
<meta charset="utf-8">
<title>Ember — Task Force Ember</title>
<link rel="stylesheet" href="https://fonts.googleapis.com/css2?family=Poppins:wght@600;700&family=Barlow:wght@500;600&family=Roboto:wght@400;500&display=swap">
<style>
:root{
  --ember:#e0461f;
  --ink:#2b2a27;
  --grey:#8a8a8a;
  --paper:#ffffff;
  --night:#050505;
  --chip:#e6e6e6;
  --text:#1f1f1f;
}
*{margin:0;padding:0;box-sizing:border-box}
html,body{width:1200px;height:3154px;overflow:hidden;background:var(--paper)}
body{font-family:"Barlow",sans-serif;color:var(--text);position:relative}

/* hero */
.hero{position:relative;height:686px;overflow:hidden}
.hero-photo{position:absolute;inset:0;
  background:
    radial-gradient(ellipse 260px 330px at 430px 300px, rgba(120,80,60,.55), transparent 70%),
    radial-gradient(ellipse 200px 340px at 1110px 300px, rgba(120,120,125,.5), transparent 70%),
    radial-gradient(ellipse 330px 160px at 380px 660px, rgba(170,20,30,.85), transparent 75%),
    radial-gradient(ellipse 700px 400px at 600px 250px, #3c4a4b, #1a2224 80%);
}
.brand{position:absolute;left:110px;top:42px;font-family:"Poppins",sans-serif;font-weight:700;font-size:29px;color:#fff}
.menu-btn{position:absolute;left:1055px;top:39px;width:32px;height:32px;border-radius:50%;background:#e8e8e8;display:flex;flex-direction:column;justify-content:center;align-items:center;gap:3px}
.menu-btn span{display:block;width:14px;height:1.5px;background:#444}
.hero-lines{position:absolute;left:0;right:0;top:220px;text-align:center;font-family:"Poppins",sans-serif;font-weight:700;font-size:36px;line-height:56px;color:#fff;text-shadow:0 2px 8px rgba(0,0,0,.6)}
.hero-motto{position:absolute;left:0;width:1160px;top:495px;text-align:center;font-family:"Poppins",sans-serif;font-weight:700;font-size:74px;color:#fff;text-shadow:0 3px 10px rgba(0,0,0,.5)}

/* pillars */
.pillars{position:relative;height:720px}
.pillar{position:absolute;left:160px;font-weight:600;font-size:20.5px;line-height:26px;color:var(--ink)}
.pillar.p1{top:103px}
.pillar.p2{top:280px}
.pillar.p3{top:494px;line-height:34px}
.pointer{position:absolute;height:2px;background:linear-gradient(90deg,var(--ember),rgba(224,70,31,0))}
.pointer::before{content:"";position:absolute;left:-9px;top:-8px;width:18px;height:18px;border-radius:50%;background:var(--ink);border:3px solid var(--ember)}
.pointer.a{left:429px;top:121px;width:195px}
.pointer.b{left:387px;top:332px;width:105px}
.pointer.c{left:429px;top:558px;width:195px}
.wheel{position:absolute;left:524px;top:75px}

/* rules */
.rules{position:relative;height:964px;
  background:
    radial-gradient(ellipse 260px 230px at 600px 0, rgba(210,210,210,.6), transparent 75%),
    radial-gradient(ellipse 620px 140px at 600px 790px, rgba(90,90,90,.55), transparent 75%),
    linear-gradient(#141414,#050505 40%,#0c0c0c);}
.rules h2{position:absolute;left:0;right:0;top:86px;text-align:center;font-family:"Poppins",sans-serif;font-weight:700;font-size:42px;color:#fff}
.rule-list{position:absolute;left:227px;top:169px;width:746px;list-style:none}
.rule{height:70px;margin-bottom:18px;background:var(--paper);display:flex;align-items:center;padding-left:9px;font-family:"Roboto",sans-serif;font-weight:500;font-size:14px;color:var(--text)}
.rule-no{width:122px;height:50px;background:var(--chip);display:flex;align-items:center;justify-content:center;margin-right:26px}

/* faq */
.faq{position:relative;height:679px}
.faq h2{position:absolute;left:0;right:0;top:82px;text-align:center;font-family:"Poppins",sans-serif;font-weight:700;font-size:44px;color:var(--ink)}
.faq-grid{position:absolute;left:111px;top:170px;width:978px;display:grid;grid-template-columns:472px 472px;column-gap:34px;row-gap:17.5px;list-style:none}
.faq-item{height:70px;background:var(--paper);box-shadow:0 3px 14px rgba(0,0,0,.09);display:flex;align-items:center;padding-left:29px;font-family:"Roboto",sans-serif;font-weight:500;font-size:13.5px;color:var(--text)}
.faq-item::before{content:"";width:3px;height:3px;border-radius:50%;background:var(--text);margin-right:27px}

/* footer */
.site-footer{position:relative;height:105px;background:var(--night);color:#fff;text-align:center;font-family:"Roboto",sans-serif;font-size:13.5px}
.site-footer p{padding-top:18px}
.social{display:flex;justify-content:center;gap:11px;margin-top:22px}
.social a{width:29px;height:29px;border:1.5px solid #fff;border-radius:50%;display:block}
</style>
</head>
<body>

<header class="hero">
  <div class="hero-photo" role="img" aria-label="Photo: two boxers training in a smoky gym, one throwing a punch at a pad held by the coach"></div>
  <div class="brand">Ember</div>
  <div class="menu-btn" aria-label="Menu"><span></span><span></span><span></span></div>
  <h1 class="hero-lines">Cole built himself an army.<br>Why was Cole Varden building an army?<br>To what purpose? For what greater good?</h1>
  <p class="hero-motto">In Cole we trust.</p>
</header>

<section class="pillars">
  <p class="pillar p1">Without Pain<br>Without Sacrifice<br>We Would have nothing</p>
  <p class="pillar p2">Success is its<br>Own reward<br>so we celebrate<br>Propration</p>
  <p class="pillar p3">When the fight was over,<br>nothing was solved, but<br>nothing wattered, we all<br>felt sevel</p>
  <span class="pointer a"></span><span class="pointer b"></span><span class="pointer c"></span>

  <svg class="wheel" width="527" height="527" viewBox="-215 -215 430 430" font-family="Roboto, sans-serif">
    <g fill="none" stroke-width="44">
      <path d="M-166.6 70.7 A181 181 0 0 1 -6.3 -180.9" stroke="#e0461f"/>
      <path d="M6.3 -180.9 A181 181 0 0 1 153.5 95.9" stroke="#2b2a27"/>
      <path d="M150.1 101.2 A181 181 0 0 1 -164 76.5" stroke="#8a8a8a"/>
    </g>
    <circle r="152" fill="#fff" stroke="#e2e2e2" stroke-width="1"/>
    <g stroke="#fff" stroke-width="4">
      <path d="M0 0 L0 -148 A148 148 0 0 1 95.1 -113.4Z" fill="#e0461f"/>
      <path d="M0 0 L95.1 -113.4 A148 148 0 0 1 145.8 -25.7Z" fill="#fff"/>
      <path d="M0 0 L145.8 -25.7 A148 148 0 0 1 128.2 74Z" fill="#2b2a27"/>
      <path d="M0 0 L128.2 74 A148 148 0 0 1 50.6 139.1Z" fill="#e0461f"/>
      <path d="M0 0 L50.6 139.1 A148 148 0 0 1 -50.6 139.1Z" fill="#fff"/>
      <path d="M0 0 L-50.6 139.1 A148 148 0 0 1 -128.2 74Z" fill="#2b2a27"/>
      <path d="M0 0 L-128.2 74 A148 148 0 0 1 -145.8 -25.7Z" fill="#e0461f"/>
      <path d="M0 0 L-145.8 -25.7 A148 148 0 0 1 -95.1 -113.4Z" fill="#fff"/>
      <path d="M0 0 L-95.1 -113.4 A148 148 0 0 1 0 -148Z" fill="#2b2a27"/>
    </g>
    <circle r="6" fill="#fff"/>
    <g font-size="8.5">
      <g transform="rotate(-70)" fill="#fff"><text x="34" y="-2">Lorem ipsum dolor sit</text><text x="34" y="8">amet, consectetur</text></g>
      <g transform="rotate(-30)" fill="#2b2a27"><text x="34" y="-2">Lorem ipsum dolor sit</text><text x="34" y="8">amet, consectetur</text></g>
      <g transform="rotate(10)" fill="#fff"><text x="34" y="-2">Lorem ipsum dolor sit</text><text x="34" y="8">amet, consectetur</text></g>
      <g transform="rotate(50)" fill="#fff"><text x="34" y="-2">Lorem ipsum dolor sit</text><text x="34" y="8">amet, consectetur</text></g>
      <g transform="rotate(90)" fill="#2b2a27"><text x="34" y="-2">Lorem ipsum dolor sit</text><text x="34" y="8">amet, consectetur</text></g>
      <g transform="rotate(130)" fill="#fff"><text x="34" y="-2">Lorem ipsum dolor sit</text><text x="34" y="8">amet, consectetur</text></g>
      <g transform="rotate(170)" fill="#fff"><text x="34" y="-2">Lorem ipsum dolor sit</text><text x="34" y="8">amet, consectetur</text></g>
      <g transform="rotate(210)" fill="#2b2a27"><text x="34" y="-2">Lorem ipsum dolor sit</text><text x="34" y="8">amet, consectetur</text></g>
      <g transform="rotate(250)" fill="#fff"><text x="34" y="-2">Lorem ipsum dolor sit</text><text x="34" y="8">amet, consectetur</text></g>
    </g>
    <g fill="#fff" font-size="15">
      <text transform="translate(-150 -91) rotate(-55)" text-anchor="middle">SPIRIT</text>
      <text transform="translate(157 -86) rotate(60)" text-anchor="middle">TECHNICAL MIND</text>
      <text x="0" y="183" text-anchor="middle">BODY</text>
    </g>
  </svg>
</section>

<section class="rules">
  <h2>I dont Want to die without any scars</h2>
  <ol class="rule-list">
    <li class="rule"><span class="rule-no">Rule No : 01</span>You do not talk about Task Force Ember.</li>
    <li class="rule"><span class="rule-no">Rule No : 02</span>You do not talk about Task Force Ember.</li>
    <li class="rule"><span class="rule-no">Rule No : 03</span>You do not contest close matches.&nbsp; (it should not have been that close)</li>
    <li class="rule"><span class="rule-no">Rule No : 04</span>You attend teammate matches whenever available/reasonable.</li>
    <li class="rule"><span class="rule-no">Rule No : 05</span>You protect the reputation of past, present, and future TFE athletes.</li>
    <li class="rule"><span class="rule-no">Rule No : 06</span>You will commit to the development of "active" TFE athletes.</li>
    <li class="rule"><span class="rule-no">Rule No : 07</span>You will compete in "Grand Slam" tournaments whenever practical and possible.</li>
    <li class="rule"><span class="rule-no">Rule No : 08</span>You will serve as the bridge between adult and children WGJF competitors.</li>
  </ol>
</section>

<section class="faq">
  <h2>Common Questions</h2>
  <ul class="faq-grid">
    <li class="faq-item">Do we want athlete profiles on our website?</li>
    <li class="faq-item">What is the criteria for acceptance?</li>
    <li class="faq-item">Should we limit membership?&nbsp; If so, by what measures</li>
    <li class="faq-item">How do you get kicked out?</li>
    <li class="faq-item">Once you get a patch, can it be taken away?</li>
    <li class="faq-item">How do we score/weight challenges?</li>
    <li class="faq-item">How do you earn the patch?</li>
    <li class="faq-item">What rewards, financial or otherwise, are offered?</li>
    <li class="faq-item">Who invites new members?</li>
    <li class="faq-item">Are we okay sharing/training across gyms?</li>
  </ul>
</section>

<footer class="site-footer">
  <p>© Copyrights 2023 Company name | All Rights reserved</p>
  <nav class="social">
    <a aria-label="Social link one"></a>
    <a aria-label="Social link two"></a>
    <a aria-label="Social link three"></a>
    <a aria-label="Social link four"></a>
  </nav>
</footer>

</body>
</html>
```